New business logo / Business Card Design

My company provides Interim Management and consultancy, for Facilities Services. Covers any aspect of facilities management, including M&E, helpdesk, asset management, supplier relationships, catering, cleaning etc. Company provides innovative solutions to exceed client needs, drawing on years of experience. Initial thoughts on logo are attached below. Fits with RAG status on projects, red, amber and green, with logo design colours around moving services from amber to green.

Target Market(s)

Facilities Management clients and service providers

Industry/Entity Type

Business

Contact Information for Business Card

Company Name = k7Rventures Ltd My name on card = Derek Whitcombe, Director Mobile = 07516309842 Email = Derek@k7rventuresltd.co.uk Twitter = @k7Rventures Ltd

Font styles to use
Sans Serif

Colors
f37122
00a990

Requirements
Must have
• Logo to be evident, with some background image in reference to Facilities Management

```html
<!DOCTYPE html>
<html lang="en">
<head>
<meta charset="utf-8">
<title>k7Rventures Ltd – Business Card</title>
<link rel="stylesheet" href="https://fonts.googleapis.com/css2?family=Quicksand:wght@500;700&display=swap">
<style>
  :root {
    --backdrop: #e9e6e1;
    --card-white: #f3f3f3;
    --card-dark: #2f2e2e;
    --card-edge: #3a3939;
    --amber: #f37122;
    --green: #00a990;
    --fold-green: #0f7a3c;
    --text-light: #f2f2f2;
    --text-muted: #b9b9b9;
    --rule-dark: #4a4848;
  }
  * { box-sizing: border-box; margin: 0; padding: 0; }
  html, body {
    width: 1200px; height: 800px; overflow: hidden;
    background: var(--backdrop);
    font-family: "Quicksand", "Helvetica Neue", Arial, sans-serif;
  }
  .card {
    position: absolute; left: 150px; top: 140px;
    width: 900px; height: 520px;
    border-radius: 18px; overflow: hidden;
    background: var(--card-dark);
    box-shadow: 0 10px 30px rgba(0,0,0,.18);
  }
  .card__edge {
    position: absolute; left: 0; top: 0; bottom: 0; width: 46px;
    background: var(--card-edge);
  }
  .card__face {
    position: absolute; left: 46px; top: 0; bottom: 0; width: 400px;
    background: var(--card-white);
    display: flex; align-items: center; justify-content: center; gap: 12px;
  }
  .brand-mark {
    width: 18px; height: 18px; border-radius: 50%;
    background: var(--amber); flex: none;
  }
  .brand-name {
    font-weight: 700; font-size: 34px; letter-spacing: 0;
    color: var(--green); white-space: nowrap;
  }
  .card__panel {
    position: absolute; left: 446px; top: 0; right: 0; bottom: 0;
    background: var(--card-dark);
  }
  .tab-fold {
    position: absolute; left: 440px; width: 14px; height: 14px;
    background: var(--fold-green);
  }
  .tab-fold--top { top: 52px; border-radius: 10px 0 0 0; }
  .tab-fold--bottom { top: 454px; border-radius: 0 0 0 10px; }
  .icon-tab {
    position: absolute; left: 440px; top: 60px;
    width: 64px; height: 400px;
    background: var(--amber);
    border-radius: 0 12px 12px 0;
  }
  .icon {
    position: absolute; left: 12px; width: 40px; height: 40px;
  }
  .contact {
    position: absolute; left: 536px; right: 40px;
    color: var(--text-light);
    font-weight: 500; font-size: 19px; letter-spacing: .3px;
    white-space: nowrap;
  }
  .contact__name { top: 92px; font-size: 23px; font-weight: 700; letter-spacing: .6px; }
  .contact__role {
    display: block; font-size: 14px; font-weight: 500;
    color: var(--text-muted); letter-spacing: 1.5px; margin-top: 2px;
  }
  .contact__phone { top: 190px; }
  .contact__email { top: 284px; }
  .contact__social { top: 376px; }
  .rule {
    position: absolute; left: 536px; right: 38px; height: 1px;
    background: var(--rule-dark);
  }
  .rule--name { top: 164px; }
  .rule--phone { top: 250px; background: var(--amber); }
  .rule--email { top: 344px; }
</style>
</head>
<body>
  <div class="card">
    <div class="card__edge"></div>
    <div class="card__face">
      <span class="brand-mark"></span>
      <span class="brand-name">Northwell Interim</span>
    </div>
    <div class="card__panel"></div>

    <div class="tab-fold tab-fold--top"></div>
    <div class="tab-fold tab-fold--bottom"></div>
    <div class="icon-tab">
      <svg class="icon" style="top:42px" viewBox="0 0 40 40" aria-label="Name">
        <circle cx="20" cy="20" r="18" fill="none" stroke="#fff" stroke-width="1.6"/>
        <circle cx="20" cy="16" r="5" fill="#fff"/>
        <path d="M11 29c1-5 5-7 9-7s8 2 9 7z" fill="#fff"/>
      </svg>
      <svg class="icon" style="top:130px" viewBox="0 0 40 40" aria-label="Phone">
        <circle cx="20" cy="20" r="18" fill="none" stroke="#fff" stroke-width="1.6"/>
        <path d="M11 17c0-3 4-4 9-4s9 1 9 4v2h-5v-2h-8v2h-5z" fill="#fff"/>
        <rect x="13" y="20" width="14" height="8" rx="1.5" fill="#fff"/>
      </svg>
      <svg class="icon" style="top:224px" viewBox="0 0 40 40" aria-label="Email">
        <circle cx="20" cy="20" r="18" fill="none" stroke="#fff" stroke-width="1.6"/>
        <g fill="none" stroke="#fff" stroke-width="1.4">
          <circle cx="20" cy="20" r="9"/>
          <ellipse cx="20" cy="20" rx="4" ry="9"/>
          <line x1="11" y1="20" x2="29" y2="20"/>
        </g>
      </svg>
      <svg class="icon" style="top:316px" viewBox="0 0 40 40" aria-label="Social handle">
        <circle cx="20" cy="20" r="18" fill="none" stroke="#fff" stroke-width="1.6"/>
        <circle cx="20" cy="20" r="7" fill="#fff"/>
      </svg>
    </div>

    <p class="contact contact__name">Derek Whitcombe<span class="contact__role">DIRECTOR</span></p>
    <div class="rule rule--name"></div>
    <p class="contact contact__phone">07516309842</p>
    <div class="rule rule--phone"></div>
    <p class="contact contact__email">Derek@k7rventuresltd.co.uk</p>
    <div class="rule rule--email"></div>
    <p class="contact contact__social">@k7Rventures Ltd</p>
  </div>
</body>
</html>
```